EVENT TENT DESIGN/ Revamping our Bi-fold Brochure/ Creating Tri Fold Brochure

Hello, I uploaded a pdf that shows the breakdown of our current brochure. We are having a hard time getting the colors correct. We want the front and back as well as any other gradient areas to be closer to our colors on the "Lumera Color Code and Font" document we uploaded.

We also feel like the solar images, outdated or the colors are a little too dull. We want more modern images with panels that are black on black or very very very navy/black blue worst case scenario.

In addition, we feel as the though some of the fonts and banners feel a little basic.

We are looking for somebody to add that modern feel to the brochure as well as turn the information into a trifold.

I will be uploading the brand page with colors and fonts, our logo, and the current book we have made. thank you in advance.

Lastly we need a "Refer a Friend" Page in the brochure. Please use the below link for inspiration. We are currently running a promo on our website, on our Brochure we like the referral pay out as follows.
https://www.trykelvaraenergy.com/refer-a-friend
You receive $35 for each qualified friend. Your qualified friend will get $25.
Get $500 when they go solar; $250 when they get a new roof.!

here is a link to our website. www.trykelvaraenergy.com
______________________________________________

Hello I increased the Winnings so that i can increase the scope of the project. I am uploading the tent measurements and a base template for you to work with. If you are a designer and have already created a Brochure for me and your design hasn't been deleted that means you are in the running for the winnings. I would like you to apply those elements to the tent design.

If you are a new designer. Use the elements that i want for the brochure and trifold and apply that to a Tent design.

my goal is to pick a designer by EOBD Thursday Aug 24th, 2023. Thank you
Updates

Colors
E54698
E96AAD
F1A4CE
F9D9EA
FCEFF6
A7469A
B969AE
D3A5CF
EDDBEB
F8F0F9
6B429C
8869AF
B7A5CE
E3DAEB
F3F0F8

Requirements
Must have
• Bi Fold Brochure Design, Tri-Fold Brochure, Event Tent Design

```html
<!DOCTYPE html>
<html lang="en">
<head>
<meta charset="utf-8">
<title>Lumera Event Tent</title>
<link href="https://fonts.googleapis.com/css2?family=Michroma&display=swap" rel="stylesheet">
<style>
  :root {
    --canopy: #f032ff;
    --canopy-deep: #d000ff;
    --canopy-light: #ff5cff;
    --brand-violet: #b020f0;
    --ink: #3b3b3b;
    --wall-grey: #c4c3c4;
    --wall-white: #e6e6e6;
    --sky-top: #1e8fe0;
    --sky-mid: #8fd0f0;
    --haze: #f2f6f8;
    --panel-dark: #3a3d42;
    --page: #ffffff;
  }
  * { margin: 0; padding: 0; box-sizing: border-box; }
  html, body { width: 1200px; height: 1200px; overflow: hidden; background: var(--page); }
  .canvas { position: relative; width: 1200px; height: 1200px; font-family: "Michroma", sans-serif; }

  .roof { position: absolute; left: 90px; top: 140px; width: 1020px; height: 300px; }

  .valance {
    position: absolute; left: 90px; top: 430px; width: 1020px; height: 90px;
    background: linear-gradient(90deg, var(--canopy) 0%, var(--canopy) 80%, var(--canopy-deep) 100%);
  }

  .wall {
    position: absolute; top: 520px; height: 480px;
    display: flex; flex-direction: column; align-items: center; justify-content: center;
  }
  .wall--left { left: 90px; width: 300px; background: var(--wall-grey); }
  .wall--back { left: 400px; width: 420px; overflow: hidden; }
  .wall--right { left: 830px; width: 280px; background: var(--wall-white); }

  .backdrop {
    position: absolute; inset: 0;
    background: linear-gradient(170deg, var(--sky-top) 0%, var(--sky-mid) 30%, var(--haze) 55%, #b9bcc0 72%, var(--panel-dark) 100%);
  }

  .brand { position: relative; display: flex; flex-direction: column; align-items: center; gap: 10px; }
  .brand-mark { width: 46px; height: 46px; border-radius: 50%; background: var(--brand-violet); margin-bottom: 14px; }
  .brand-name { font-size: 28px; letter-spacing: 5px; color: var(--ink); }
  .brand-tagline { font-size: 9px; letter-spacing: 2px; color: var(--ink); white-space: nowrap; }

  .wall--back .brand { margin-top: -150px; }
  .wall--back .brand-mark { width: 60px; height: 60px; }
  .wall--back .brand-name { font-size: 34px; }
  .wall--back .brand-tagline { font-size: 10px; }

  .wall--right .brand-name { font-size: 24px; }
  .wall--right .brand-tagline { font-size: 8px; }
</style>
</head>
<body>
<main class="canvas">
  <svg class="roof" viewBox="0 0 1020 300" aria-hidden="true">
    <defs>
      <linearGradient id="roofShade" x1="0" y1="0" x2="0" y2="1">
        <stop offset="0" stop-color="var(--canopy)"/>
        <stop offset="1" stop-color="var(--canopy-light)"/>
      </linearGradient>
    </defs>
    <path d="M0 290 Q300 200 500 10 Q520 0 540 10 Q760 200 1020 290 L1020 300 L0 300 Z" fill="url(#roofShade)"/>
  </svg>

  <div class="valance"></div>

  <section class="wall wall--left">
    <div class="brand">
      <span class="brand-mark"></span>
      <span class="brand-name">LUMERA</span>
      <span class="brand-tagline">SOLAR | ROOFING | CONSTRUCTION</span>
    </div>
  </section>

  <section class="wall wall--back">
    <div class="backdrop" role="img" aria-label="Photo of a bright blue cloudy sky above rows of dark solar panels on a roof"></div>
    <div class="brand">
      <span class="brand-mark"></span>
      <span class="brand-name">LUMERA</span>
      <span class="brand-tagline">SOLAR | ROOFING | CONSTRUCTION</span>
    </div>
  </section>

  <section class="wall wall--right">
    <div class="brand">
      <span class="brand-mark"></span>
      <span class="brand-name">LUMERA</span>
      <span class="brand-tagline">SOLAR | ROOFING | CONSTRUCTION</span>
    </div>
  </section>
</main>
</body>
</html>
```